Tranvik Leasing Corp - Business Card Design

Need a new modern designed business card that is different and stands out to represent my equipment financing company. Tranvik Leasing Corp finances all types of equipment and all types of industries. We like to do equipment financing a different way by putting customers first and want our card to represent that different approach to business. I want a card that some remembers when they receive it so it sticks in their mind and makes that wow impression.

Card should have a black background so the logo stands out. It can be horizontial or vertical or a combination of both.

Front of card information is below that shows the information that would go on my card. That is where I want a different look or design to stand out. The front could be split black/orange colour so the logo could pop on black side and information on orange side with different lettering. Just outside the box thinking on the front of the card. Open to any type of design.

Back of card is below which i I like unless you have a different spin to provide or a different idea that would make the card better as I am open to anything that looks great.

Target Market(s)

Tranvik Leasing Corp deals with business owners in all industries.

Industry/Entity Type

Business

Contact Information for Business Card

Colors

Designer to choose colors to be used in the design.

Requirements
Must have
• Modern
• Different
• Stand Out
• Makes an Impression

```html
<!DOCTYPE html>
<html lang="en">
<head>
<meta charset="utf-8">
<title>Tranvik Leasing Corp – Business Card</title>
<link rel="stylesheet" href="https://fonts.googleapis.com/css2?family=Lato:wght@400;700&display=swap">
<style>
  :root {
    --stage: #e9e6e1;
    --card-black: #070707;
    --texture-dark: #1f1f1f;
    --texture-mid: #3a3a3a;
    --brand-orange: #f7711e;
    --brand-red: #e8192c;
    --ink-dark: #111111;
    --ink-light: #ffffff;
  }
  * { margin: 0; padding: 0; box-sizing: border-box; }
  html, body {
    width: 1200px;
    height: 800px;
    overflow: hidden;
    background: var(--stage);
    font-family: "Lato", Arial, sans-serif;
  }
  .stage {
    position: relative;
    width: 1200px;
    height: 800px;
  }
  .card {
    position: absolute;
    top: 250px;
    width: 520px;
    height: 300px;
    background: var(--card-black);
    overflow: hidden;
    box-shadow: 0 10px 24px rgba(0,0,0,0.25);
  }
  .card-back { left: 50px; }
  .card-front { left: 630px; }
  .card-art {
    position: absolute;
    inset: 0;
    width: 520px;
    height: 300px;
  }

  /* Back side */
  .back-brand {
    position: absolute;
    left: 0;
    right: 0;
    top: 130px;
    display: flex;
    align-items: center;
    justify-content: center;
    gap: 12px;
  }
  .brand-dot {
    width: 22px;
    height: 22px;
    border-radius: 50%;
    background: var(--brand-orange);
  }
  .brand-name {
    font-weight: 700;
    font-size: 28px;
    letter-spacing: 1px;
    color: var(--brand-orange);
  }

  /* Front side */
  .holder {
    position: absolute;
    left: 26px;
    top: 60px;
    color: var(--ink-dark);
  }
  .holder-name { font-size: 24px; font-weight: 700; line-height: 1.1; }
  .holder-title { font-size: 16px; font-weight: 700; line-height: 1.3; }

  .contact-list {
    position: absolute;
    left: 28px;
    top: 182px;
    list-style: none;
    color: var(--ink-light);
    font-size: 14px;
  }
  .contact-item {
    display: flex;
    align-items: center;
    gap: 10px;
    height: 22px;
  }
  .contact-icon { width: 14px; height: 14px; }

  .front-brand {
    position: absolute;
    right: 24px;
    top: 186px;
    display: flex;
    align-items: center;
    gap: 8px;
  }
  .front-brand .brand-dot { width: 14px; height: 14px; }
  .front-brand .brand-name { font-size: 16px; letter-spacing: 0.5px; }

  .website {
    position: absolute;
    right: 26px;
    top: 252px;
    color: var(--ink-light);
    font-size: 14px;
  }
</style>
</head>
<body>
<main class="stage">

  <section class="card card-back" aria-label="Card back">
    <svg class="card-art" viewBox="0 0 520 300" aria-hidden="true">
      <polygon points="0,0 18,0 18,42 32,56 32,244 18,258 18,300 0,300" fill="var(--brand-red)"/>
      <polygon points="520,0 502,0 502,42 488,56 488,244 502,258 502,300 520,300" fill="var(--brand-red)"/>
    </svg>
    <div class="back-brand">
      <span class="brand-dot"></span>
      <span class="brand-name">Tranvik Leasing Corp</span>
    </div>
  </section>

  <section class="card card-front" aria-label="Card front">
    <svg class="card-art" viewBox="0 0 520 300">
      <defs>
        <linearGradient id="band-gradient" x1="0" y1="0" x2="1" y2="0">
          <stop offset="0" stop-color="var(--brand-orange)"/>
          <stop offset="1" stop-color="var(--brand-red)"/>
        </linearGradient>
        <linearGradient id="texture-gradient" x1="0" y1="0" x2="1" y2="1">
          <stop offset="0" stop-color="var(--texture-mid)"/>
          <stop offset="1" stop-color="var(--texture-dark)"/>
        </linearGradient>
      </defs>
      <polygon role="img" aria-label="Dark speckled stone texture"
               points="0,0 470,0 470,60 420,60 360,170 0,170" fill="url(#texture-gradient)"/>
      <polygon class="name-band" points="0,48 380,48 340,124 0,124" fill="url(#band-gradient)"/>
      <polygon class="base-band" points="0,222 150,222 196,280 520,280 520,300 0,300" fill="url(#band-gradient)"/>
    </svg>

    <div class="holder">
      <p class="holder-name">Dario Pellman</p>
      <p class="holder-title">President</p>
    </div>

    <ul class="contact-list">
      <li class="contact-item">
        <svg class="contact-icon" viewBox="0 0 24 24" aria-hidden="true">
          <path fill="var(--brand-orange)" d="M6.6 10.8a15 15 0 0 0 6.6 6.6l2.2-2.2a1 1 0 0 1 1-.25 11.4 11.4 0 0 0 3.6.57 1 1 0 0 1 1 1V20a1 1 0 0 1-1 1A17 17 0 0 1 3 4a1 1 0 0 1 1-1h3.5a1 1 0 0 1 1 1c0 1.25.2 2.45.57 3.57a1 1 0 0 1-.25 1z"/>
        </svg>
        <span>403.555.0142</span>
      </li>
      <li class="contact-item">
        <svg class="contact-icon" viewBox="0 0 24 24" aria-hidden="true">
          <rect x="2" y="5" width="20" height="14" rx="1.5" fill="var(--brand-orange)"/>
          <polyline points="3,6 12,13 21,6" fill="none" stroke="var(--card-black)" stroke-width="1.8"/>
        </svg>
        <span>dario@tranvikleasing.ca</span>
      </li>
    </ul>

    <div class="front-brand">
      <span class="brand-dot"></span>
      <span class="brand-name">Tranvik Leasing Corp</span>
    </div>

    <p class="website">www.tranvikleasing.ca</p>
  </section>

</main>
</body>
</html>
```